Looking for a high-end business card design for a construction company

We are looking to update our business card design. We are a post-frame construction company that builds custom buildings, commercial spaces, homes, and anything else. We have multiple people working here so we would need something we can easily customize the information for the specific person. We need a name, website, cell phone, office phone as well as social icons. Our colors are black, white, and grey/silver so I would love a black background or something that is more striking than just a traditional white business card. Looking for something that is very professional with a high-end look/feel. I have attached our logos, they can be silver, white, grey, or black.
Industry/Entity Type
Construction
Contact Information for Business Card
Business logo, Name, Cell phone, Office phone, website, social Icons
Colors
Designer to choose only greyscale colors for use in the design.
Look and feel

```html
<!DOCTYPE html>
<html lang="en">
<head>
<meta charset="utf-8">
<title>Harlow Builders, Inc. — Business Card</title>
<link rel="stylesheet" href="https://fonts.googleapis.com/css2?family=Open+Sans:wght@400;600;700&display=swap">
<style>
  :root {
    --backdrop: #c8c8c8;
    --card-dark: #3a3838;
    --card-dark-deep: #2f2d2d;
    --pattern-tone: #4a4848;
    --paper: #ffffff;
    --ring: #5c5a5a;
    --ink: #2b2929;
    --text-light: #f4f4f4;
    --text-muted: #d9d9d9;
    --dot-1: #6f6f6f;
    --dot-2: #8a8a8a;
    --dot-3: #a3a3a3;
  }
  * { box-sizing: border-box; margin: 0; padding: 0; }
  html, body {
    width: 1200px;
    height: 815px;
    overflow: hidden;
    background: var(--backdrop);
    font-family: "Open Sans", Arial, sans-serif;
  }
  .stage {
    position: relative;
    width: 1200px;
    height: 815px;
  }
  .card {
    position: absolute;
    left: 320px;
    width: 560px;
    height: 320px;
    border-radius: 22px;
    overflow: hidden;
    background: var(--card-dark);
    box-shadow: 0 10px 26px rgba(0,0,0,0.28);
  }
  .card--front { top: 70px; }
  .card--back  { top: 425px; }

  .front-shapes {
    position: absolute;
    inset: 0;
  }

  .brand-block {
    position: absolute;
    left: 300px;
    top: 58px;
    width: 230px;
    text-align: center;
    color: var(--ink);
  }
  .brand-name {
    font-weight: 700;
    font-size: 30px;
    letter-spacing: 3px;
    line-height: 1.1;
    text-transform: uppercase;
  }
  .brand-sub {
    font-weight: 700;
    font-size: 15px;
    letter-spacing: 3px;
    line-height: 1.3;
    text-transform: uppercase;
  }
  .social-row {
    display: flex;
    justify-content: center;
    gap: 9px;
    margin-top: 16px;
  }
  .social-dot {
    width: 18px;
    height: 18px;
    border-radius: 50%;
    background: var(--dot-2);
  }
  .social-dot:nth-child(odd) { background: var(--dot-1); }
  .social-dot:nth-child(3) { background: var(--dot-3); }

  .person {
    position: absolute;
    left: 34px;
    top: 118px;
    color: var(--text-light);
  }
  .person-name {
    font-weight: 700;
    font-size: 25px;
    letter-spacing: 0.5px;
    line-height: 1.1;
  }
  .person-role {
    font-size: 13px;
    color: var(--text-muted);
    margin-top: 2px;
  }
  .address {
    margin-top: 18px;
    font-size: 13px;
    line-height: 1.35;
    color: var(--text-light);
  }
  .contact-list {
    list-style: none;
    margin-top: 16px;
    font-size: 13px;
    line-height: 1.4;
    color: var(--text-light);
  }
  .contact-list li {
    display: flex;
    align-items: center;
    gap: 7px;
  }
  .contact-icon {
    width: 11px;
    height: 11px;
    flex: none;
  }

  .pattern-field {
    position: absolute;
    inset: 0;
    background:
      radial-gradient(ellipse at 70% 60%, var(--pattern-tone) 0%, var(--card-dark) 55%, var(--card-dark-deep) 100%);
  }
  .back-brand {
    position: absolute;
    right: 44px;
    top: 168px;
    display: flex;
    align-items: center;
    gap: 14px;
    color: var(--paper);
  }
  .back-brand-mark {
    width: 40px;
    height: 40px;
    border-radius: 50%;
    background: var(--paper);
    flex: none;
  }
  .back-brand-text {
    font-weight: 700;
    text-transform: uppercase;
    line-height: 1.1;
  }
  .back-brand-text .brand-name { font-size: 26px; letter-spacing: 3px; }
  .back-brand-text .brand-sub { font-size: 13px; letter-spacing: 2.6px; }
</style>
</head>
<body>
<main class="stage">

  <section class="card card--front" aria-label="Business card front">
    <svg class="front-shapes" width="560" height="320" viewBox="0 0 560 320" aria-hidden="true">
      <circle cx="426" cy="124" r="208" fill="var(--paper)"/>
      <circle cx="426" cy="124" r="202" fill="var(--ring)"/>
      <circle cx="436" cy="118" r="198" fill="var(--paper)"/>
    </svg>

    <div class="brand-block">
      <div class="brand-name">Harlow</div>
      <div class="brand-sub">Builders, Inc.</div>
      <div class="social-row" aria-label="Social profiles">
        <span class="social-dot"></span>
        <span class="social-dot"></span>
        <span class="social-dot"></span>
        <span class="social-dot"></span>
        <span class="social-dot"></span>
        <span class="social-dot"></span>
      </div>
    </div>

    <div class="person">
      <h1 class="person-name">Dane Porter</h1>
      <p class="person-role">Founder</p>
      <p class="address">Ridge Rd. No. 42/017,<br>Suite Two - 6150</p>
      <ul class="contact-list">
        <li>
          <svg class="contact-icon" viewBox="0 0 12 12" aria-hidden="true">
            <rect x="3" y="0.5" width="6" height="11" rx="1.2" fill="none" stroke="var(--text-light)" stroke-width="1.2"/>
            <circle cx="6" cy="9.5" r="0.7" fill="var(--text-light)"/>
          </svg>
          +012 555 0147
        </li>
        <li>
          <svg class="contact-icon" viewBox="0 0 12 12" aria-hidden="true">
            <path d="M1 4 Q6 0 11 4 L9.5 5.5 L8 4.5 L4 4.5 L2.5 5.5 Z" fill="var(--text-light)"/>
            <rect x="2.5" y="6" width="7" height="5" rx="1" fill="var(--text-light)"/>
          </svg>
          +012 555 0198
        </li>
        <li>
          <svg class="contact-icon" viewBox="0 0 12 12" aria-hidden="true">
            <rect x="0.5" y="2.5" width="11" height="7.5" rx="1" fill="var(--text-light)"/>
            <path d="M1 3 L6 7 L11 3" fill="none" stroke="var(--card-dark)" stroke-width="1"/>
          </svg>
          info@HarlowBuilders.com
        </li>
        <li>
          <svg class="contact-icon" viewBox="0 0 12 12" aria-hidden="true">
            <circle cx="6" cy="6" r="5.3" fill="none" stroke="var(--text-light)" stroke-width="1.1"/>
            <ellipse cx="6" cy="6" rx="2.2" ry="5.3" fill="none" stroke="var(--text-light)" stroke-width="0.9"/>
            <line x1="0.7" y1="6" x2="11.3" y2="6" stroke="var(--text-light)" stroke-width="0.9"/>
          </svg>
          www.HarlowBuilders.com
        </li>
      </ul>
    </div>
  </section>

  <section class="card card--back" aria-label="Business card back">
    <div class="pattern-field" role="img" aria-label="Repeating tone-on-tone company monogram pattern across the dark background"></div>
    <div class="back-brand">
      <span class="back-brand-mark" aria-hidden="true"></span>
      <div class="back-brand-text">
        <div class="brand-name">Harlow</div>
        <div class="brand-sub">Builders, Inc.</div>
      </div>
    </div>
  </section>

</main>
</body>
</html>
```